I need a business card design for a new company that will be doing consulting work around issues of cultural competency, and diversity and inclusion. I would like the design to be crisp and clear with bold but conservative colors and incorporate shades of blue

Target Market(s)

Small businesses, schools, non-profits

Industry/Entity Type

Consulting

Font styles to use
Serif
Sans Serif

Colors
0c5ba6
6b449b
3276b5
0292cd

Requirements
Must have
• A Morrow Venture (name of company)
• Lemlem Tavish
• CEO
• lemlem@amorrowventure.com
• (215)483-2756

```html
<!DOCTYPE html>
<html lang="en">
<head>
<meta charset="UTF-8">
<title>A Morrow Venture — Business Card</title>
<link rel="stylesheet" href="https://fonts.googleapis.com/css2?family=Montserrat:ital,wght@0,600;1,800&family=Merriweather:wght@400;700&display=swap">
<style>
  :root {
    --blue-deep: #2f79bd;
    --blue-bright: #1493d1;
    --purple: #6b449b;
    --white: #ffffff;
    --ink: #1b2a3a;
  }
  html, body {
    margin: 0;
    padding: 0;
    overflow: hidden;
    background: var(--blue-deep);
  }
  .card {
    position: relative;
    width: 1200px;
    height: 687px;
    overflow: hidden;
    background: var(--blue-deep);
  }
  .card__panel {
    position: absolute;
    inset: 0;
    width: 1200px;
    height: 687px;
  }
  .tilted {
    position: absolute;
    transform: rotate(-16.5deg);
    transform-origin: left bottom;
    white-space: nowrap;
    line-height: 1;
  }
  .company-name {
    left: 238px;
    top: 248px;
    font-family: "Montserrat", sans-serif;
    font-style: italic;
    font-weight: 800;
    font-size: 54px;
    color: var(--purple);
    text-shadow: 2px 2px 0 rgba(255,255,255,0.55);
  }
  .company-rule {
    left: 497px;
    top: 238px;
    width: 318px;
    height: 12px;
    background: var(--white);
  }
  .person-name {
    left: 398px;
    top: 352px;
    font-family: "Merriweather", serif;
    font-weight: 700;
    font-size: 44px;
    color: var(--white);
    text-shadow: 3px 3px 2px rgba(20,30,50,0.75);
  }
  .person-title {
    left: 410px;
    top: 408px;
    font-family: "Montserrat", sans-serif;
    font-weight: 600;
    font-size: 30px;
    color: var(--white);
  }
  .title-rule {
    left: 410px;
    top: 452px;
    width: 146px;
    height: 11px;
    background: var(--purple);
  }
  .contact {
    display: flex;
    align-items: center;
    gap: 16px;
    font-family: "Merriweather", serif;
    font-size: 31px;
    color: var(--white);
  }
  .contact--email { left: 522px; top: 438px; }
  .contact--phone { left: 544px; top: 496px; }
  .contact__icon { width: 30px; height: 30px; flex: none; }
</style>
</head>
<body>
  <main class="card">
    <svg class="card__panel" viewBox="0 0 1200 687" aria-hidden="true">
      <polygon points="415,0 1200,0 1200,687 634,687" fill="var(--blue-bright)"/>
    </svg>

    <div class="tilted company-name">A Morrow Venture</div>
    <div class="tilted company-rule"></div>

    <div class="tilted person-name">Lemlem Tavish</div>
    <div class="tilted person-title">CEO</div>
    <div class="tilted title-rule"></div>

    <div class="tilted contact contact--email">
      <svg class="contact__icon" viewBox="0 0 30 30" aria-hidden="true">
        <circle cx="15" cy="15" r="13" fill="var(--ink)"/>
        <circle cx="15" cy="15" r="4.5" fill="none" stroke="var(--white)" stroke-width="2"/>
        <path d="M19.5 11 v6 a2.5 2.5 0 0 0 5 0 v-2 a9.5 9.5 0 1 0 -4 7.7" fill="none" stroke="var(--white)" stroke-width="2"/>
      </svg>
      <span>lemlem@amorrowventure.com</span>
    </div>

    <div class="tilted contact contact--phone">
      <svg class="contact__icon" viewBox="0 0 30 30" aria-hidden="true">
        <circle cx="15" cy="15" r="13" fill="var(--ink)"/>
        <path d="M10 8 l3 0 l1.5 4 l-2 1.5 a9 9 0 0 0 4 4 l1.5 -2 l4 1.5 l0 3 a2 2 0 0 1 -2 2 a13 13 0 0 1 -12 -12 a2 2 0 0 1 2 -2z" fill="var(--white)"/>
      </svg>
      <span>(215)483-2756</span>
    </div>
  </main>
</body>
</html>
```